Executive search firm in fashion, luxury and retail industry needs logo and card design.

We are a start-up recruiting firm that specializes in the retail and fashion industry, based in New York. We are looking for something that will appeal to CEO level clients and candidates, but that has a little design edge...not overly corporate but still CEO-appropriate. We have clean, sophisticated taste and want a contemporary feel. Happy to have a two sided card. Not afraid of a little color but it should be high-design, not gimmicky and tasteful.

Quillby Market(s)

CEO's, HR Leaders, in retail, fashion (i.e. Havenmere, Quillby, Otto Vasquel)

Industry/Entity Type

Professional Service

Contact Information for Business Card

Linden Row Talent Partners
Address to be determined
New York, NY 10036

Marla Tovick
Managing Director
(555)013-2846
mtovick@lindenrowtalent.example

Font styles to use
Serif
Sans Serif

Requirements
Must have
• clean lines, crisp graphics, some color. Prefer a graphic treatment over a "logo" per se. No pictures, etc.
Nice to have
• double sided design.
Should not have
• Gimmicks, smaltz, goop. Think Gallery of Current Forms, not the Pelham Vault. No earth tones, as in beige and brown, no pastels. Strong colors are fine in moderation. Grays are good. Jewel tones are good. No red.

```html
<!DOCTYPE html>
<html lang="en">
<head>
<meta charset="utf-8">
<title>Linden Row Talent Partners — Business Card</title>
<link rel="stylesheet" href="https://fonts.googleapis.com/css2?family=Jost:wght@400;500;600&display=swap">
<style>
  :root {
    --backdrop: #8b8b8b;
    --paper: #e9eaec;
    --navy: #05507a;
    --steel: #8d8f92;
    --ink: #3a3a3a;
    --mist: #e4e6e8;
  }
  * { box-sizing: border-box; margin: 0; padding: 0; }
  html, body {
    width: 1200px;
    height: 781px;
    overflow: hidden;
    background: var(--backdrop);
    font-family: "Jost", "Futura", sans-serif;
  }
  .canvas { position: relative; width: 1200px; height: 781px; }

  .card {
    position: absolute;
    left: 358px;
    width: 452px;
    height: 250px;
    overflow: hidden;
  }
  .card--front { top: 104px; background: var(--paper); }
  .card--back  { top: 408px; background: var(--navy); }

  .wordmark {
    position: absolute;
    right: 28px;
    top: 42px;
    text-align: right;
    font-weight: 500;
    text-transform: uppercase;
    line-height: 1;
  }
  .wordmark__name { display: block; font-size: 23px; letter-spacing: 2.2px; }
  .wordmark__tag  { display: block; font-size: 12px; letter-spacing: 1.6px; margin-top: 7px; }
  .card--front .wordmark { color: var(--navy); }
  .card--back  .wordmark { color: var(--mist); }

  .holder {
    position: absolute;
    left: 29px;
    top: 174px;
    line-height: 1;
  }
  .holder__name {
    font-weight: 600;
    font-size: 14px;
    letter-spacing: 0.4px;
    text-transform: uppercase;
    color: var(--navy);
  }
  .holder__title {
    margin-top: 5px;
    font-size: 11.5px;
    color: var(--ink);
  }

  .contacts {
    position: absolute;
    right: 28px;
    top: 174px;
    list-style: none;
    text-align: right;
    font-size: 11px;
    color: var(--ink);
  }
  .contacts li {
    display: flex;
    justify-content: flex-end;
    align-items: center;
    gap: 9px;
    height: 14.5px;
  }
  .contacts svg { width: 11px; height: 11px; flex: none; }

  .accent-band {
    position: absolute;
    left: 0;
    bottom: 0;
    width: 452px;
    height: 10px;
    display: block;
  }

  .site-url {
    position: absolute;
    right: 41px;
    top: 206px;
    font-size: 11.5px;
    color: var(--mist);
    letter-spacing: 0.2px;
  }
</style>
</head>
<body>
<main class="canvas">

  <section class="card card--front" aria-label="Card front">
    <div class="wordmark">
      <span class="wordmark__name">Linden Row</span>
      <span class="wordmark__tag">Talent Partners</span>
    </div>

    <div class="holder">
      <p class="holder__name">Marla Tovick</p>
      <p class="holder__title">Managing Director</p>
    </div>

    <ul class="contacts">
      <li>(555)013-2846
        <svg viewBox="0 0 11 11" aria-hidden="true">
          <rect width="11" height="11" rx="1.5" fill="var(--navy)"/>
          <path d="M3 2.2c.5-.3.9-.2 1.1.2l.6 1.2c.1.3 0 .6-.3.8l-.4.3c.3.8.9 1.5 1.7 1.9l.3-.4c.2-.3.5-.4.8-.2l1.1.6c.4.2.4.7.1 1.1-.6.7-1.4.9-2.3.4C4.3 7.2 3 5.7 2.6 4.1c-.2-.8 0-1.5.4-1.9z" fill="#fff"/>
        </svg>
      </li>
      <li>mtovick@lindenrowtalent.example
        <svg viewBox="0 0 11 11" aria-hidden="true">
          <rect width="11" height="11" rx="1.5" fill="var(--navy)"/>
          <rect x="2" y="3" width="7" height="5" fill="none" stroke="#fff" stroke-width="0.9"/>
          <path d="M2 3l3.5 3L9 3" fill="none" stroke="#fff" stroke-width="0.9"/>
        </svg>
      </li>
      <li>www.lindenrowtalent.example
        <svg viewBox="0 0 11 11" aria-hidden="true">
          <rect width="11" height="11" rx="1.5" fill="var(--navy)"/>
          <circle cx="5.5" cy="5.5" r="3.4" fill="none" stroke="#fff" stroke-width="0.8"/>
          <ellipse cx="5.5" cy="5.5" rx="1.4" ry="3.4" fill="none" stroke="#fff" stroke-width="0.7"/>
          <path d="M2.1 5.5h6.8M2.6 3.9h5.8M2.6 7.1h5.8" stroke="#fff" stroke-width="0.6"/>
        </svg>
      </li>
    </ul>

    <svg class="accent-band" viewBox="0 0 452 10" preserveAspectRatio="none" aria-hidden="true">
      <polygon points="0,0 176,0 167,10 0,10" fill="var(--navy)"/>
      <polygon points="183,0 452,0 452,10 174,10" fill="var(--steel)"/>
    </svg>
  </section>

  <section class="card card--back" aria-label="Card back">
    <div class="wordmark">
      <span class="wordmark__name">Linden Row</span>
      <span class="wordmark__tag">Talent Partners</span>
    </div>
    <p class="site-url">www.lindenrowtalent.example</p>
  </section>

</main>
</body>
</html>
```